Clear Harbor Transportation Management Association

We are looking to design an awards certificate for an upcoming event that we are having in December. This award would be given to our employee members who have done an outstanding job of promoting commuting alternatives (biking, walking, transit, ridesharing) to driving alone, and as such have reduced green house gas emissions. We are looking for a cool graphic that will make the award something special and worth framing. Attached is our current logo which should be on the certificate somewhere, as well as a few of our program design logos which can be used for inspiration.

Target Market(s)

Board members

Industry/Entity Type

Event

Requirements
Must have
• Graphic suitable for framing as part of an awards certificate
Nice to have
• Something that relates to what we do which is promoting sustainable tranportation (biking, walking, transit, and ridesharing).

```html
<!DOCTYPE html>
<html lang="en">
<head>
<meta charset="utf-8">
<title>Clear Harbor TMA Award Certificate</title>
<link href="https://fonts.googleapis.com/css2?family=Tinos:wght@400;700&family=Open+Sans:wght@600;700&display=swap" rel="stylesheet">
<style>
  :root{
    --teal:#1fa89a;
    --blue:#1a86c4;
    --paper:#f5f3ec;
    --paper-edge:#e2ddcf;
    --ink:#3a3a3a;
    --text:#1c1c1c;
    --gold:#f2c93a;
    --icon-blue:#8cc9e8;
  }
  html,body{margin:0;padding:0;overflow:hidden;background:#fff;}
  .certificate{position:relative;width:1200px;height:927px;overflow:hidden;font-family:"Tinos","Times New Roman",serif;color:var(--text);}
  .frame-ornament{position:absolute;left:12px;top:6px;width:1176px;height:915px;border-radius:18px;
    background:linear-gradient(120deg,var(--teal) 0%,var(--blue) 50%,var(--teal) 100%);}
  .paper{position:absolute;left:80px;top:62px;width:1040px;height:804px;background:var(--paper);
    box-shadow:inset 0 0 40px var(--paper-edge);}
  .title{position:absolute;left:0;width:1200px;top:140px;margin:0;text-align:center;font-weight:700;font-size:96px;letter-spacing:1px;color:var(--ink);line-height:1;}
  .presented{position:absolute;left:0;width:1200px;top:254px;text-align:center;font-size:19px;letter-spacing:2.6px;}
  .name-line{position:absolute;left:204px;top:376px;width:784px;height:0;border-top:1.5px solid var(--text);}
  .citation{position:absolute;left:204px;top:393px;width:784px;margin:0;text-align:center;font-size:20px;line-height:27px;}
  .modes{position:absolute;left:226px;top:491px;display:flex;gap:24px;}
  .mode{width:58px;height:58px;border-radius:10px;border:2px solid var(--icon-blue);border-right-color:var(--gold);border-bottom-color:var(--gold);background:#fbfaf6;display:flex;align-items:center;justify-content:center;}
  .mode svg{width:38px;height:38px;}
  .org-name{position:absolute;left:752px;top:478px;width:240px;font-size:30px;font-weight:700;line-height:34px;color:var(--text);}
  .ribbon{position:absolute;left:80px;top:647px;width:1040px;height:38px;
    background:linear-gradient(90deg,var(--teal),var(--blue) 45%,var(--blue) 60%,var(--teal));
    border-top:2px solid var(--gold);}
  .seal{position:absolute;left:490px;top:578px;width:176px;height:176px;}
  .sign-row{position:absolute;top:766px;font-size:19px;display:flex;align-items:flex-end;}
  .sign-row span.rule{display:inline-block;border-bottom:1.5px solid var(--text);margin-left:6px;margin-bottom:4px;}
  .date{left:160px;}
  .date .rule{width:268px;}
  .signature{left:670px;}
  .signature .rule{width:228px;}
</style>
</head>
<body>
<main class="certificate">
  <div class="frame-ornament" role="img" aria-label="Ornate teal and blue filigree border"></div>
  <div class="paper"></div>

  <h1 class="title">CERTIFICATE</h1>
  <div class="presented">THIS CERTIFICATE IS PRESENTED TO</div>
  <div class="name-line"></div>
  <p class="citation">Lorem ipsum dolor sit amet, consectetuer adipiscing elit. Aenean commodo ligula eget dolor.</p>

  <div class="modes">
    <div class="mode" aria-label="Biking"><svg viewBox="0 0 40 40"><circle cx="10" cy="28" r="6" fill="none" stroke="#222" stroke-width="2"/><circle cx="30" cy="28" r="6" fill="none" stroke="#222" stroke-width="2"/><circle cx="25" cy="8" r="3" fill="#222"/><path d="M10 28 L18 20 L24 13 L28 20 L30 28 M18 20 L24 28" fill="none" stroke="#222" stroke-width="3" stroke-linecap="round"/></svg></div>
    <div class="mode" aria-label="Rail transit"><svg viewBox="0 0 40 40"><rect x="10" y="5" width="20" height="25" rx="4" fill="#222"/><rect x="13" y="10" width="14" height="8" fill="#fff"/><circle cx="15" cy="24" r="2" fill="#fff"/><circle cx="25" cy="24" r="2" fill="#fff"/><path d="M12 37 L16 31 M28 37 L24 31" stroke="#222" stroke-width="2"/></svg></div>
    <div class="mode" aria-label="Shuttle bus"><svg viewBox="0 0 40 40"><rect x="3" y="12" width="34" height="15" rx="3" fill="#222"/><g fill="#fff"><rect x="6" y="15" width="5" height="5"/><rect x="13" y="15" width="5" height="5"/><rect x="20" y="15" width="5" height="5"/><rect x="27" y="15" width="6" height="5"/></g><circle cx="11" cy="28" r="3" fill="#fff" stroke="#222" stroke-width="2"/><circle cx="29" cy="28" r="3" fill="#fff" stroke="#222" stroke-width="2"/></svg></div>
    <div class="mode" aria-label="Ferry"><svg viewBox="0 0 40 40"><path d="M5 24 L35 24 L31 31 L9 31 Z" fill="none" stroke="#222" stroke-width="2"/><rect x="11" y="16" width="18" height="8" fill="none" stroke="#222" stroke-width="2"/><rect x="17" y="9" width="6" height="7" fill="#222"/><path d="M4 35 Q10 32 16 35 T28 35 T38 35" fill="none" stroke="#222" stroke-width="1.5"/></svg></div>
    <div class="mode" aria-label="Walking and running"><svg viewBox="0 0 40 40"><circle cx="24" cy="6" r="3.5" fill="#222"/><path d="M14 16 L22 12 L26 20 L32 22 M22 12 L18 24 L26 30 L24 37 M18 24 L12 34 L6 34" fill="none" stroke="#222" stroke-width="4" stroke-linecap="round" stroke-linejoin="round"/></svg></div>
    <div class="mode" aria-label="Ridesharing car"><svg viewBox="0 0 40 40"><path d="M8 20 L12 11 L28 11 L32 20 Z" fill="none" stroke="#222" stroke-width="2.5"/><rect x="5" y="19" width="30" height="10" rx="3" fill="#222"/><circle cx="11" cy="24" r="2" fill="#fff"/><circle cx="29" cy="24" r="2" fill="#fff"/><rect x="8" y="29" width="5" height="4" fill="#222"/><rect x="27" y="29" width="5" height="4" fill="#222"/></svg></div>
  </div>

  <div class="org-name">Clear Harbor TMA</div>

  <div class="ribbon"></div>

  <svg class="seal" viewBox="0 0 176 176" aria-label="2015 Award seal">
    <defs>
      <linearGradient id="seal-fill" x1="0" y1="0" x2="0" y2="1">
        <stop offset="0" stop-color="#1fa89a"/>
        <stop offset="1" stop-color="#1a86c4"/>
      </linearGradient>
    </defs>
    <circle cx="88" cy="88" r="78" fill="#1fa89a" stroke="#1fa89a" stroke-width="14" stroke-dasharray="8 6"/>
    <circle cx="88" cy="88" r="60" fill="url(#seal-fill)" stroke="#fff" stroke-width="6" stroke-dasharray="5 3"/>
    <circle cx="88" cy="88" r="52" fill="url(#seal-fill)"/>
    <line x1="48" y1="92" x2="128" y2="92" stroke="#bfe6ea" stroke-width="1"/>
    <text x="88" y="86" text-anchor="middle" font-family="Open Sans, Arial, sans-serif" font-weight="700" font-size="27" fill="#fff">2015</text>
    <text x="88" y="112" text-anchor="middle" font-family="Open Sans, Arial, sans-serif" font-weight="600" font-size="15" fill="#fff">AWARD</text>
  </svg>

  <div class="sign-row date">DATE<span class="rule"></span></div>
  <div class="sign-row signature">SIGNATURE<span class="rule"></span></div>
</main>
</body>
</html>
```